Flyer advertising our coaching program for our indoor golf facility

A editable (word document) and pdf version of a flyer advertising our coaching program for our indoor golf training facility. The flyer should look similar to the uploaded examples. The flyer should be the colors red, light grey, white, and black. It should also have our Fairway Nine Golf logo on it and the following text:Fairway Nine Golf CoachingAwarded Winning NLB Coaching / Use of Tour Technology Included / Birchview, KEL RollDesk, Motion Harbor. Online Scheduling Coaching Membership Options:6months $2500- 2 lessons a month- 1 practice session a week- Fairway Nine hat- 1 playing session*Pay up front cash or check & save $75or $417/month. (3month minimum) 12months $4500-2 lessons a month-1 practice session a week- 2 playing sessions- Fairway Nine Golf bag*Pay up front cash or check and save $225or $375/month. (3month minimum) Special offer:First 10 who sign up for a full-year membership save $500Contact us for more information: info@fairwayninegolf.example / www.fairwayninegolf.example

Target Market(s)

golf

Font styles to use
Sans Serif

Colors

Designer to choose only greyscale colors for use in the design.

Requirements
Must have
• Red, light grey, white, black, our logo. word document and pdf version

```html
<!DOCTYPE html>
<html lang="en">
<head>
<meta charset="utf-8">
<title>Fairway Nine Golf Coaching Flyer</title>
<link rel="stylesheet" href="https://fonts.googleapis.com/css2?family=Roboto+Condensed:wght@700&family=Questrial&family=Poppins:wght@500;600&display=swap">
<style>
  :root{
    --red:#e8392f;
    --ink:#1c1510;
    --white:#ffffff;
    --grey:#9b9b9b;
    --text:#222222;
    --grass:#6f9a45;
  }
  *{margin:0;padding:0;box-sizing:border-box}
  html,body{width:1200px;height:1200px;overflow:hidden;background:var(--grey)}
  .stage{position:relative;width:1200px;height:1200px}
  .flyer{
    position:absolute;left:172px;top:0;width:954px;height:1337px;
    transform:scale(0.8975);transform-origin:0 0;
    background:var(--white);overflow:hidden;
    font-family:"Questrial",sans-serif;color:var(--text);
  }
  .flyer-art{position:absolute;left:0;top:0}
  .abs{position:absolute}
  .brand-ring{left:166px;top:50px;width:160px;height:160px;border:7px solid var(--red);border-radius:50%}
  .brand-name{left:0;width:492px;top:222px;text-align:center;font-family:"Poppins",sans-serif;font-weight:600;font-size:34px;color:var(--red)}
  .headline{left:44px;top:296px;color:var(--white);font-family:"Roboto Condensed",sans-serif;font-weight:700;line-height:1}
  .headline .line1{display:block;font-size:47px;letter-spacing:.5px}
  .headline .line2{display:block;font-size:90px;margin-top:8px}
  .feature{top:566px;width:260px;text-align:center;font-size:19px;line-height:22px}
  .feature .icon{width:70px;height:70px;margin:0 auto 24px;background:var(--red);border-radius:50%;opacity:.9}
  .feature.one{left:11px}.feature.two{left:314px}.feature.three{left:647px}
  .divider{top:569px;height:118px;border-left:2px dotted #555}
  .pill-cta{left:265px;top:749px;width:424px;height:50px;border-radius:25px;background:var(--red);color:var(--white);
    font-family:"Roboto Condensed",sans-serif;font-weight:700;font-size:36px;line-height:50px;text-align:center;
    box-shadow:0 10px 8px -6px rgba(0,0,0,.35)}
  .section-title{font-family:"Poppins",sans-serif;font-weight:500;color:var(--red);font-size:27px}
  .section-title::after{content:"";display:block;width:52px;height:3px;background:var(--red);margin-top:4px}
  .options-title{left:45px;top:836px}
  .offer-title{left:61px;top:1173px}
  .term{height:30px;border-radius:15px;background:var(--red);color:var(--white);font-family:"Poppins",sans-serif;font-weight:500;
    font-size:20px;line-height:30px;padding:0 14px}
  .term.six{left:45px;top:907px}.term.twelve{left:536px;top:912px}
  .perks{list-style:none;font-size:18px}
  .perks li{height:28px;display:flex;align-items:center;gap:8px}
  .perks svg{flex:none}
  .perks.six{left:62px;top:946px}.perks.twelve{left:553px;top:952px}
  .rule{height:0;border-top:2px dotted #444}
  .rule.six{left:64px;top:1071px;width:341px}.rule.twelve{left:548px;top:1071px;width:349px}
  .note{font-size:15.5px;line-height:19px}
  .note.six{left:64px;top:1080px}.note.twelve{left:548px;top:1080px}
  .offer-lead{left:60px;top:1234px;font-size:17px}
  .offer-main{left:60px;top:1256px;font-family:"Poppins",sans-serif;font-weight:600;font-size:27px;color:#111}
  .offer-main .amount{color:var(--red)}
  .contact{right:42px;text-align:right;color:var(--white);display:flex;align-items:center;justify-content:flex-end;gap:10px;white-space:nowrap}
  .contact.phone{top:1200px;font-family:"Roboto Condensed",sans-serif;font-weight:700;font-size:40px}
  .contact.mail{top:1255px;font-size:19px}
  .contact.web{top:1294px;font-size:15px}
</style>
</head>
<body>
<div class="stage">
  <div class="flyer">
    <svg class="flyer-art" width="954" height="1337" viewBox="0 0 954 1337">
      <defs>
        <linearGradient id="photoTone" x1="0" y1="0" x2="0" y2="1">
          <stop offset="0" stop-color="#e9ece6"/>
          <stop offset=".3" stop-color="#4d6b3a"/>
          <stop offset=".5" stop-color="var(--grass)"/>
          <stop offset="1" stop-color="#5f8a3a"/>
        </linearGradient>
      </defs>
      <path d="M0 0H954V644C760 520 650 470 480 468C300 466 120 500 0 559Z" fill="var(--ink)"/>
      <path d="M0 559C120 500 300 466 480 468C650 470 760 520 954 644V600C780 480 650 432 480 430C300 428 120 456 0 512Z" fill="var(--red)"/>
      <path d="M410 0H954V590C800 550 660 510 560 420C450 320 400 150 410 0Z" fill="var(--red)"/>
      <path role="img" aria-label="Photo: golf coach guiding a student's swing on a driving range" d="M450 0H954V560C810 525 690 495 600 430C500 350 440 170 450 0Z" fill="url(#photoTone)"/>
      <path d="M954 1337H420C500 1212 670 1128 850 1128C900 1128 930 1133 954 1140Z" fill="var(--red)"/>
      <path d="M954 1337H445C525 1232 690 1150 850 1150C900 1150 930 1156 954 1164Z" fill="var(--ink)"/>
    </svg>

    <div class="abs brand-ring"></div>
    <div class="abs brand-name">Fairway Nine Golf</div>
    <h1 class="abs headline"><span class="line1">FAIRWAY NINE GOLF</span><span class="line2">COACHING</span></h1>

    <div class="abs feature one"><div class="icon" role="img" aria-label="Coaching icon"></div>NLB Coaching</div>
    <div class="abs divider" style="left:272px"></div>
    <div class="abs feature two"><div class="icon" role="img" aria-label="Technology icon"></div>Use of Tour Technology<br>Included</div>
    <div class="abs divider" style="left:616px"></div>
    <div class="abs feature three"><div class="icon" role="img" aria-label="Golfer icon"></div>Birchview, KEL RollDesk,<br>Motion Harbor.</div>

    <div class="abs pill-cta">ONLINE SCHEDULING</div>

    <h2 class="abs section-title options-title">Coaching Membership Options:</h2>

    <div class="abs term six">6months</div>
    <ul class="abs perks six">
      <li><svg width="14" height="14" viewBox="0 0 14 14"><circle cx="7" cy="7" r="5.5" fill="none" stroke="#e8392f" stroke-width="1.6"/><path d="M4 7l2.5 2.5L13 2" fill="none" stroke="#e8392f" stroke-width="1.8"/></svg>$2500- 2 lessons a month</li>
      <li><svg width="14" height="14" viewBox="0 0 14 14"><circle cx="7" cy="7" r="5.5" fill="none" stroke="#e8392f" stroke-width="1.6"/><path d="M4 7l2.5 2.5L13 2" fill="none" stroke="#e8392f" stroke-width="1.8"/></svg>1 practice session a week</li>
      <li><svg width="14" height="14" viewBox="0 0 14 14"><circle cx="7" cy="7" r="5.5" fill="none" stroke="#e8392f" stroke-width="1.6"/><path d="M4 7l2.5 2.5L13 2" fill="none" stroke="#e8392f" stroke-width="1.8"/></svg>Fairway Nine hat</li>
      <li><svg width="14" height="14" viewBox="0 0 14 14"><circle cx="7" cy="7" r="5.5" fill="none" stroke="#e8392f" stroke-width="1.6"/><path d="M4 7l2.5 2.5L13 2" fill="none" stroke="#e8392f" stroke-width="1.8"/></svg>1 playing session</li>
    </ul>
    <div class="abs rule six"></div>
    <p class="abs note six">*Pay up front cash or check &amp; save $75or<br>$417/month. (3month minimum)</p>

    <div class="abs term twelve">12months</div>
    <ul class="abs perks twelve">
      <li><svg width="14" height="14" viewBox="0 0 14 14"><circle cx="7" cy="7" r="5.5" fill="none" stroke="#e8392f" stroke-width="1.6"/><path d="M4 7l2.5 2.5L13 2" fill="none" stroke="#e8392f" stroke-width="1.8"/></svg>$4500-2 lessons a month</li>
      <li><svg width="14" height="14" viewBox="0 0 14 14"><circle cx="7" cy="7" r="5.5" fill="none" stroke="#e8392f" stroke-width="1.6"/><path d="M4 7l2.5 2.5L13 2" fill="none" stroke="#e8392f" stroke-width="1.8"/></svg>1 practice session a week</li>
      <li><svg width="14" height="14" viewBox="0 0 14 14"><circle cx="7" cy="7" r="5.5" fill="none" stroke="#e8392f" stroke-width="1.6"/><path d="M4 7l2.5 2.5L13 2" fill="none" stroke="#e8392f" stroke-width="1.8"/></svg>2 playing sessions</li>
      <li><svg width="14" height="14" viewBox="0 0 14 14"><circle cx="7" cy="7" r="5.5" fill="none" stroke="#e8392f" stroke-width="1.6"/><path d="M4 7l2.5 2.5L13 2" fill="none" stroke="#e8392f" stroke-width="1.8"/></svg>Fairway Nine Golf bag</li>
    </ul>
    <div class="abs rule twelve"></div>
    <p class="abs note twelve">*Pay up front cash or check and save $225or<br>$375/month. (3month minimum)</p>

    <h2 class="abs section-title offer-title">Special offer:</h2>
    <p class="abs offer-lead">First 10 who sign up for a full-year</p>
    <p class="abs offer-main">membership save <span class="amount">$500</span></p>

    <div class="abs contact phone">555-014-2288
      <svg width="22" height="40" viewBox="0 0 22 40"><path d="M6 2c6 2 12 8 12 18S12 36 6 38l-2-6c3-1 7-5 7-12S7 9 4 8z" fill="#e8392f"/></svg>
    </div>
    <div class="abs contact mail">info@fairwayninegolf.example
      <svg width="22" height="14" viewBox="0 0 22 14"><rect x="1" y="1" width="20" height="12" fill="#fff"/><path d="M1 1l10 7 10-7" fill="none" stroke="#1c1510" stroke-width="1.5"/></svg>
    </div>
    <div class="abs contact web">visit us for more information www.fairwayninegolf.example</div>
  </div>
</div>
</body>
</html>
```